Criação de Papelaria Profissional para Construção & Engenharia
" Empresa que atua em incorporação imobiliária, administrando a construção de edifícios "

```html
<!DOCTYPE html>
<html lang="pt-BR">
<head>
<meta charset="UTF-8">
<title>Torres Aguiar Engenharia — Cartão de Visita</title>
<link href="https://fonts.googleapis.com/css2?family=Michroma&display=swap" rel="stylesheet">
<style>
  :root {
    --brand-blue: #1d4a8c;
    --brand-blue-dark: #163a70;
    --steel-gray: #8a8f96;
    --light-gray: #c9ccd1;
    --text-dark: #4b4f55;
    --card-white: #ffffff;
    --backdrop: #e9ebee;
  }
  * { margin: 0; padding: 0; box-sizing: border-box; }
  html, body {
    width: 1200px; height: 1200px; overflow: hidden;
    background: var(--backdrop);
    font-family: "Michroma", "Arial", sans-serif;
  }
  .stationery {
    position: relative; width: 1200px; height: 1200px;
  }
  .card {
    position: absolute; left: 150px; width: 900px; height: 500px;
    background: var(--card-white);
    box-shadow: 0 6px 22px rgba(0,0,0,0.18);
    overflow: hidden;
  }
  .card--front { top: 70px; }
  .card--back { top: 630px; }

  /* Front */
  .front-brand {
    position: absolute; left: 170px; top: 150px;
    display: flex; align-items: center; gap: 26px;
  }
  .brand-square {
    width: 110px; height: 110px; background: var(--brand-blue);
  }
  .brand-name {
    font-size: 42px; color: var(--brand-blue); letter-spacing: 2px; line-height: 1;
  }
  .brand-tagline {
    margin-top: 14px; font-size: 15px; color: var(--steel-gray); letter-spacing: 16px;
  }
  .front-band {
    position: absolute; left: 0; bottom: 0; width: 900px; height: 80px;
  }
  .front-site {
    position: absolute; left: 0; right: 0; bottom: 18px; text-align: center;
    color: #fff; font-size: 17px; letter-spacing: 5px;
  }

  /* Back */
  .back-panel {
    position: absolute; left: 0; top: 0; width: 340px; height: 235px;
    background: var(--brand-blue);
  }
  .back-brand {
    position: absolute; left: 380px; top: 52px;
  }
  .back-brand .brand-name { font-size: 32px; }
  .back-brand .brand-tagline { font-size: 12px; letter-spacing: 13px; margin-top: 10px; }
  .contact-list {
    position: absolute; left: 380px; top: 175px; list-style: none;
  }
  .contact-item {
    display: flex; align-items: flex-start; gap: 16px;
    font-size: 16px; color: var(--text-dark); letter-spacing: 1.5px;
    margin-bottom: 14px; line-height: 1.4;
  }
  .contact-icon { width: 22px; height: 22px; flex: none; margin-top: 1px; }
  .back-edge {
    position: absolute; right: 0; top: 0; width: 70px; height: 500px;
  }
</style>
</head>
<body>
<main class="stationery">

  <section class="card card--front" aria-label="Frente do cartão">
    <div class="front-brand">
      <div class="brand-square"></div>
      <div>
        <div class="brand-name">TORRES AGUIAR</div>
        <div class="brand-tagline">ENGENHARIA</div>
      </div>
    </div>
    <svg class="front-band" viewBox="0 0 900 80" aria-hidden="true">
      <polygon points="60,20 840,20 900,80 0,80" fill="var(--light-gray)"/>
      <polygon points="150,34 750,34 790,80 110,80" fill="var(--brand-blue)"/>
    </svg>
    <div class="front-site">WWW.SITE.COM.BR</div>
  </section>

  <section class="card card--back" aria-label="Verso do cartão">
    <div class="back-panel"></div>
    <div class="back-brand">
      <div class="brand-name">TORRES AGUIAR</div>
      <div class="brand-tagline">ENGENHARIA</div>
    </div>
    <ul class="contact-list">
      <li class="contact-item">
        <svg class="contact-icon" viewBox="0 0 24 24" aria-hidden="true">
          <circle cx="12" cy="12" r="11" fill="var(--brand-blue)"/>
          <path d="M8.5 6.5l2 3-1.2 1.3a7 7 0 0 0 3.9 3.9l1.3-1.2 3 2-1 2.2c-5 0-10-5-10-10z" fill="#fff"/>
        </svg>
        <span>+00 00-0000-0000</span>
      </li>
      <li class="contact-item">
        <svg class="contact-icon" viewBox="0 0 24 24" aria-hidden="true">
          <rect x="2" y="5" width="20" height="14" rx="2" fill="var(--brand-blue)"/>
          <path d="M3 6l9 7 9-7" stroke="#fff" stroke-width="1.6" fill="none"/>
        </svg>
        <span>contato@torresaguiar.com.br</span>
      </li>
      <li class="contact-item">
        <svg class="contact-icon" viewBox="0 0 24 24" aria-hidden="true">
          <path d="M12 1a8 8 0 0 0-8 8c0 6 8 14 8 14s8-8 8-14a8 8 0 0 0-8-8z" fill="var(--brand-blue)"/>
          <circle cx="12" cy="9" r="3" fill="#fff"/>
        </svg>
        <span>End. Completo - Nº - Bairro<br>Cidade - CEP - Estado - UF</span>
      </li>
    </ul>
    <svg class="back-edge" viewBox="0 0 70 500" aria-hidden="true">
      <polygon points="40,0 70,0 70,500 40,500 20,250" fill="var(--light-gray)"/>
      <polygon points="56,40 70,40 70,460 56,460 46,250" fill="var(--brand-blue)"/>
    </svg>
  </section>

</main>
</body>
</html>
```